Hand sanitizer logos and bottle design

Want a very simple and clean logo for - PURA42.
Need a badge logo for - Clean Shield 42 Keeper.
Need bottle label designed. Mock up is attached. Keep it very clean as in mockup.
Target Market(s)
retail
Font styles to use
Sans Serif
Requirements
Must have
- Simple Clean

```html
<!DOCTYPE html>
<html lang="en">
<head>
<meta charset="utf-8">
<title>PURA42 Gel Hand Sanitizer Label</title>
<link href="https://fonts.googleapis.com/css2?family=Montserrat:wght@400;500;600;700;800&display=swap" rel="stylesheet">
<style>
  :root {
    --orange: #ec671e;
    --amber: #f39200;
    --blue: #2eaae1;
    --ink: #111111;
    --paper: #ffffff;
  }
  * { margin: 0; padding: 0; box-sizing: border-box; }
  html, body { width: 1200px; height: 800px; overflow: hidden; background: var(--paper); }
  body { font-family: "Montserrat", sans-serif; color: var(--ink); }
  .label {
    position: absolute;
    left: 405px;
    top: 44px;
    width: 390px;
    height: 712px;
  }
  .brand-name {
    position: absolute;
    left: 0; top: 0;
    width: 390px;
    font-weight: 700;
    font-size: 92px;
    line-height: 92px;
    color: var(--orange);
    letter-spacing: 1px;
  }
  .brand-rule {
    position: absolute;
    left: 0; top: 92px;
    width: 390px; height: 2px;
    background: var(--orange);
  }
  .protection {
    position: absolute;
    left: 0; top: 98px;
    width: 390px;
    font-weight: 800;
    font-size: 29px;
    line-height: 30px;
    color: var(--amber);
    white-space: nowrap;
  }
  .tagline {
    position: absolute;
    left: 0; top: 160px;
    width: 390px;
    text-align: center;
    font-weight: 400;
    font-size: 16.5px;
    line-height: 21px;
    text-transform: uppercase;
    letter-spacing: 0.2px;
  }
  .product-type {
    position: absolute;
    left: 0; top: 302px;
    font-weight: 600;
    font-size: 32px;
    line-height: 30px;
    color: var(--blue);
  }
  .guard-badge {
    position: absolute;
    left: 190px; top: 256px;
    width: 178px; height: 178px;
    border: 3px solid var(--blue);
    border-radius: 50%;
    display: flex;
    align-items: center;
    justify-content: center;
    text-align: center;
    font-weight: 700;
    font-size: 19px;
    line-height: 24px;
    color: var(--blue);
  }
  .certificate-mark {
    position: absolute;
    left: 290px; top: 436px;
    width: 76px; height: 44px;
    background: var(--ink);
  }
  .features {
    position: absolute;
    left: 0; top: 532px;
    list-style: none;
    font-weight: 500;
    font-size: 25px;
    line-height: 26px;
  }
  .net-content {
    position: absolute;
    left: 110px; top: 676px;
    display: flex;
    align-items: flex-end;
    gap: 6px;
  }
  .net-content .net-label {
    font-size: 12px;
    line-height: 11px;
    font-weight: 400;
  }
  .net-content .net-volume {
    font-size: 34px;
    line-height: 32px;
    font-weight: 500;
  }
</style>
</head>
<body>
  <main class="label">
    <h1 class="brand-name">PURA42</h1>
    <div class="brand-rule"></div>
    <p class="protection">12 HOURS PROTECTION</p>
    <p class="tagline">Nanotechnology enables one use<br>that will not dry out your skin.</p>
    <p class="product-type">GEL HAND<br>SANITIZER</p>
    <div class="guard-badge">Clean Shield<br>42 Keeper</div>
    <div class="certificate-mark" role="img" aria-label="Certification badge"></div>
    <ul class="features">
      <li>Non Toxic</li>
      <li>Alchool Free</li>
      <li>Extended Protection</li>
      <li>Kills 99.99% of Viruses</li>
    </ul>
    <div class="net-content">
      <span class="net-label">CONT.<br>NET</span>
      <span class="net-volume">500 ML</span>
    </div>
  </main>
</body>
</html>
```